Regional Showdown Flyer for Holiday Program

Need a one page flyer, can be back to front or one page, ensuring you can fit all information, colourful, aimed at a market of 8-13 year old boys and girls.
The flyer needs to be noticed, needs to have certain information on it and needs to be Autralian Rule Football orientated.
Have uploaded file so you can understand the style (not content), style of flyer I am looking at getting submitted.

Target Market(s)

8-13 year old boys and girls and their parents.

Requirements
Must have
• Regional Showdown Event
• Price for Regional Showdown Day will be $85
• Strictly Limited Places, only the best footballers should enter this challenge
• Inaugural event, be the first Regional Showdown Winner for your age!
• Do you love a challenge! Put yourself to the test!
• Are you up to it - Water Slide Goal Kicking Contest! The fastest kick in the West (tested by our very own speed gun)! Can you survive the Footy Titan Trail or Last One Standing Goal Kicking! These challenges are crazy are super fun!
• If you think you can deliver on the big stage then this is for YOU!
• All District age winners will receive prizes, awards and the adulation from all their peers!
• Year's 3-5 from 9am to 12pm
• Year's 6-8 from 1-4pm
• All challengers compete against their own age
• Lunch Provided
• Monday 16th April - Upper Tarrowby Regional Showdown Day at Tarrowby Oval
• Tuesday 17th April - North Tarrowby Regional Showdown Day at Kilmorna Reserve
• Wednesday 18th April - Yarlo Regional Showdown Day - Dunhaven Football Club
• Every Challenge Participant receives a District Football!
• Need to put all 3 District Football Logos on the bottom of the flyer, logos attached at bottom.
Nice to have
• Plenty of colour, if you can fit all information on one page that would be fine
Should not have
• Dull, boring, any footballs should be Aussie Rules footballs not NFL or soccer

```html
<!DOCTYPE html>
<html lang="en">
<head>
<meta charset="utf-8">
<title>Regional Showdown Flyer</title>
<link rel="stylesheet" href="https://fonts.googleapis.com/css2?family=Lilita+One&family=Bangers&family=Open+Sans:ital,wght@0,400;0,600;0,700;1,400;1,600;1,700&display=swap">
<style>
:root{
  --sky-top:#1568b8;
  --sky-bottom:#2ba3e2;
  --orange:#f47a20;
  --orange-light:#ffb347;
  --green:#8cc63f;
  --green-dark:#1fa24a;
  --band-blue:#1ba0df;
  --purple:#4f2d8c;
  --purple-soft:#8a6cc0;
  --lilac:#c9b8ec;
  --ink-purple:#4a2a8a;
  --ink-blue:#1d7cc4;
  --ink-grey:#333;
  --white:#fff;
}
*{margin:0;padding:0;box-sizing:border-box}
html,body{width:927px;height:1200px;overflow:hidden;background:#fff}
.flyer{position:relative;width:927px;height:1200px;overflow:hidden;
  background:linear-gradient(180deg,var(--sky-top) 0%,var(--sky-bottom) 75%);
  font-family:"Open Sans",Arial,sans-serif;color:var(--white)}
.headline{position:absolute;left:0;width:927px;text-align:center;
  font-family:"Lilita One","Arial Black",sans-serif;letter-spacing:2px;line-height:1;
  color:var(--orange);-webkit-text-stroke:3px var(--white);paint-order:stroke fill;
  text-shadow:4px 5px 6px rgba(0,0,0,.35)}
.headline--one{top:52px;font-size:104px}
.headline--two{top:144px;font-size:96px}
.tagline{position:absolute;top:244px;left:0;width:927px;text-align:center;
  font-style:italic;font-weight:600;font-size:52px;letter-spacing:-1px;
  text-shadow:3px 3px 5px rgba(0,0,0,.35)}
.splash{position:absolute;left:-40px;top:330px;width:560px;height:560px;border-radius:46% 54% 40% 60%;
  background:radial-gradient(circle at 45% 55%,var(--purple-soft) 0%,#7c5fb8 45%,rgba(244,122,32,.85) 75%,rgba(244,122,32,0) 100%)}
.ball{position:absolute;left:78px;top:448px;width:380px;height:256px;border-radius:50%;
  transform:rotate(-32deg);background:radial-gradient(ellipse at 40% 35%,#ff5a4a 0%,#e8252a 55%,#b81418 100%);
  box-shadow:6px 10px 18px rgba(0,0,0,.35)}
.price{position:absolute;top:372px;left:690px;font-style:italic;font-weight:700;font-size:62px;
  text-shadow:3px 3px 5px rgba(0,0,0,.35)}
.band{position:absolute;right:0;text-align:right;padding-right:30px}
.band--green{top:440px;left:498px;height:68px;background:linear-gradient(90deg,var(--green) 0%,var(--green-dark) 100%);
  clip-path:polygon(6% 0,100% 0,100% 100%,0 100%)}
.band--blue{top:508px;left:478px;height:124px;background:var(--band-blue)}
.band--purple{top:632px;left:460px;height:276px;background:var(--purple)}
.band-title{font-family:"Bangers",Impact,sans-serif;font-size:33px;letter-spacing:1px;line-height:1;padding-top:8px}
.band-note{font-style:italic;font-weight:600;font-size:15px}
.band-lead{font-style:italic;font-size:22px;line-height:1.45}
.prizes{font-style:italic;font-size:15px;color:var(--lilac);line-height:1.45;padding-top:22px}
.session{font-style:italic;font-size:24px;color:var(--lilac);line-height:1.35}
.session-note{font-style:italic;font-size:15px;color:var(--lilac)}
.callout{font-family:"Bangers",Impact,sans-serif;font-size:27px;letter-spacing:1px;line-height:1.2;padding-top:22px}
.contest{position:absolute;left:60px;width:360px;text-align:center;font-style:italic;font-weight:600;font-size:13px;
  text-shadow:1px 1px 2px rgba(0,0,0,.4)}
.contest small{display:block;font-size:8.5px;font-weight:600}
.contest--slide{top:758px;left:70px}
.contest--trail{top:806px}
.footer{position:absolute;left:0;top:908px;width:927px;height:292px;
  background:linear-gradient(180deg,#f7f8fa 0%,#fff 40%,#e9ebee 100%)}
.footer::before{content:"";position:absolute;top:0;left:0;width:100%;height:10px;background:linear-gradient(90deg,#e8f4fb,var(--band-blue))}
.clubs{position:absolute;top:42px;left:48px;width:860px;display:flex;justify-content:space-between;align-items:center}
.club{display:flex;align-items:center;gap:12px;font-family:"Open Sans",Arial,sans-serif;font-weight:700;font-size:22px;color:var(--ink-blue)}
.club-mark{width:54px;height:54px;border-radius:50%;background:var(--ink-blue)}
.schedule{position:absolute;top:182px;left:20px;width:652px;text-align:right;font-size:17.5px;color:var(--ink-grey);line-height:1.45}
.schedule b{color:var(--ink-purple);font-style:italic;font-weight:700}
.divider{position:absolute;top:178px;left:682px;width:3px;height:94px;background:var(--ink-blue)}
.perks{position:absolute;top:184px;left:690px;width:206px;text-align:right;font-style:italic;color:var(--ink-blue)}
.perks p{font-size:14px;line-height:1.45}
.perks strong{display:block;font-size:24px;font-weight:600;padding-top:6px}
</style>
</head>
<body>
<main class="flyer">
  <h1 class="headline headline--one">DO YOU LOVE</h1>
  <h1 class="headline headline--two">A CHALLENGE?</h1>
  <p class="tagline">PUT YOURSELF TO THE TEST!</p>

  <div class="splash" role="img" aria-label="Colourful paint splatter in purple, lime and orange"></div>
  <div class="ball" role="img" aria-label="Red Aussie Rules football printed with Regional Showdown Event"></div>

  <p class="price">$85</p>

  <section class="band band--green">
    <p class="band-title">STRICTLY LIMITED PLACES</p>
    <p class="band-note">Only the BEST Footballers should enter this challenge</p>
  </section>
  <section class="band band--blue">
    <p class="band-title" style="padding-top:14px">INAUGURAL EVENT</p>
    <p class="band-lead">be the FIRST Regional Showdown<br>Winner for your age!</p>
  </section>
  <section class="band band--purple">
    <p class="prizes">All District age winners will receive prizes,<br>awards and the adulation from all their peers!</p>
    <p class="session">Year's 3-5 from 9am to 12pm<br>Year's 6-8 from 1-4pm</p>
    <p class="session-note">(All challengers compete against their own age group)</p>
    <p class="callout">If you think you can deliver<br>on the big stage then this is for YOU!</p>
  </section>

  <p class="contest contest--slide">Are you up to it? Water Slide Goal Kicking Contest!<small>The fastest kick in the West (tested by our very own speed gun)!</small></p>
  <p class="contest contest--trail">Can you survive the Footy Titan Trail<br>or Last One Standing Goal Kicking!<small>These challenges are crazy are super fun!</small></p>

  <footer class="footer">
    <div class="clubs">
      <div class="club"><span>Stingrays District</span><span class="club-mark"></span></div>
      <div class="club"><span>Kelpies District</span><span class="club-mark"></span></div>
      <div class="club"><span>Yarlo District</span><span class="club-mark"></span></div>
    </div>
    <div class="schedule">
      <p><b>Monday 16th April:</b> Upper Tarrowby Regional Showdown Day at Tarrowby Oval</p>
      <p><b>Tuesday 17th April:</b> North Tarrowby Regional Showdown Day at Kilmorna Reserve</p>
      <p><b>Wednesday 18th April</b>: Yarlo Regional Showdown Day - Dunhaven Football Club</p>
    </div>
    <div class="divider"></div>
    <div class="perks">
      <p>*Every Challenge Participant<br>receives a District Football!</p>
      <strong>Lunch Provided</strong>
    </div>
  </footer>
</main>
</body>
</html>
```